依頼詳細
今回は、汎用的に使える会社案内印刷物(完成サイズA4・表1~4の4ページ・4c/4c)を作成します。

形状は、2つ折に製本したサイズがA4で、右サイドにチラシを挟めるポケットが付いた形状となります。

イメージサンプルpdfおよびデザイン用テンプレート(win・mac用)を添付しますので、参考になさってください。
なお、PDFイメージサンプルは、周りに白の余白がありますが、印刷設定の不具合ですので、無視してください。また、あくまでイメージですので、あまりとらわれずにデザインしていただいても結構ですが、ポケットがある表3部分は、チラシを入れて配布するため、あまり複雑な文面の挿入は避けたいです。チラシを取ったら、驚きがあったりすると面白いかもしれません。

使用する写真・画像もご用意をお願い致します。
会社案内としてのデザイン使用権利は弊社に帰属しますので、写真画像などは、使用条件をクリアしたものをご用意ください。

複数ご提案いただいた場合は、その中より一案を採用します。
テキスト文面・ロゴについて、コンペ段階では添付サンプルのものをご利用いただきますが、依頼者決定後、若干デザインとテキストの変更をお願いする場合があります。
サイズ
A4
ページ数
4ページ
希望イメージ
シンプル 複雑
単色 カラフル
暗い 明るい
日常 高級
遊び心 厳粛
未来的 伝統的
女性的 男性的
希望する色
空色、アースカラー(夢・未来・自然・開放感)など
納品ファイル
• 高解像度JPG (.jpg)
• イラストレーター形式 (.ai)
補足説明
弊社ホームページ http://www.minatoyuzu.net
※現在のホームページは用品レンタルが中心となっていますが、今後イベントやむツアーなどの業務を拡大する予定です。
弊社ロゴ追加添付します。(ただしロゴは本番で若干変更予定です。)
ご提案ありがとうございました。
選考を行いますので、3日~1週間程度お時間を頂戴します。
恐縮ですが、少々お待ちくださいませ。
■ 選んだ理由

選定に時間がかかりすみませんでした。
皆様それぞれに良いデザインで、社内選考でも意見が分かれましたが、結果として避けられない部分があるデザインがございました。以下に理由をお知らせいたします。
・アウトドアの気持ちよさや自然の広がりを感じるもの。
・商品が写っているものは、弊社で扱わないものがあると不都合があるため難しかった。
・海や登山、海外にクローズアップしすぎると、少々弊社のターゲットとは違ってしまう。
・テキストレイアウトにバランスがあること。
・家族向けとスポーツ志向の良いバランスがあること。

■ 提案者全員のお礼・コメント

このたびは、多数のご応募ありがとうございました。
また、選考に時間がかかってしまったこと、また当選されなかった方に、お詫びを申し上げます。当選されなかった方も、それぞれ良い点があり、選考が難航いたしました。
来年も、チラシなどの作成を考えております。
また是非ご参加いただけましたら幸いです。
お礼まで。

```html
<!DOCTYPE html>
<html lang="ja">
<head>
<meta charset="utf-8">
<title>みなとゆず 会社案内</title>
<link rel="stylesheet" href="https://fonts.googleapis.com/css2?family=Noto+Sans+JP:wght@400;700&display=swap">
<style>
  :root {
    --bg: #e9e9e9;
    --paper: #ffffff;
    --ink: #5a4a3a;
    --ink-soft: #7d6e60;
    --accent: #c8862f;
    --brand: #8a5a2a;
    --rule: #cfc6bb;
    --sky-top: #4f96d6;
    --sky-mid: #b8d8ef;
    --grass-light: #9fd04a;
    --grass-dark: #3f8a1c;
    --figure: #b48a5a;
  }
  * { margin: 0; padding: 0; box-sizing: border-box; }
  html, body { width: 829px; height: 1200px; overflow: hidden; background: var(--bg); }
  body { position: relative; font-family: "Noto Sans JP", sans-serif; color: var(--ink); }

  .spread { position: absolute; left: 22px; width: 785px; background: var(--paper); }
  .spread--outer { top: 22px; height: 544px; overflow: hidden; }
  .spread--inner { top: 602px; height: 558px; border: 1px solid var(--rule); }

  .cover-photo {
    position: absolute; inset: 0;
    background: linear-gradient(180deg, var(--sky-top) 0%, var(--sky-mid) 38%, #e8f3d2 55%, var(--grass-light) 68%, var(--grass-dark) 100%);
  }
  .fold { position: absolute; left: 392px; top: 0; bottom: 0; width: 1px; background: rgba(255,255,255,.35); }

  .cover-brand { position: absolute; left: 470px; top: 200px; width: 220px; text-align: center; }
  .brand-tagline { font-size: 9px; letter-spacing: .2em; color: var(--brand); }
  .brand-name { font-size: 34px; font-weight: 700; color: var(--brand); letter-spacing: .06em; line-height: 1.3; }
  .cover-title { margin-top: 14px; font-size: 13px; letter-spacing: .4em; color: rgba(255,255,255,.85); }

  .inner-fold { position: absolute; left: 392px; top: 0; bottom: 0; width: 1px; background: var(--rule); }

  .profile { position: absolute; left: 22px; top: 16px; width: 348px; bottom: 16px; border: 1px dashed var(--rule); padding: 14px 28px; }
  .profile-heading { text-align: center; font-size: 11px; letter-spacing: .3em; color: var(--ink-soft); border-bottom: 1px solid var(--rule); padding-bottom: 6px; margin-bottom: 22px; }
  .profile-list { list-style: none; font-size: 10.5px; line-height: 1.85; color: var(--ink); }
  .profile-list .gap { height: 14px; }
  .profile-list .label { font-weight: 700; }

  .mission { position: absolute; left: 434px; top: 62px; width: 220px; }
  .mission-heading { font-size: 17px; font-weight: 700; color: var(--accent); padding-bottom: 6px; border-bottom: 1px solid var(--accent); }
  .mission-heading small { font-size: 11px; color: var(--ink-soft); font-weight: 400; }
  .mission-list { list-style: none; margin-top: 22px; }
  .mission-list li { display: flex; gap: 10px; font-size: 10.5px; line-height: 1.7; margin-bottom: 26px; color: var(--ink); }
  .mission-list .num { flex: none; width: 18px; height: 18px; border-radius: 50%; background: var(--accent); color: #fff; font-size: 10px; text-align: center; line-height: 18px; }

  .hiker { position: absolute; left: 683px; top: 100px; width: 82px; height: 236px; border-radius: 40px 40px 6px 6px; background: linear-gradient(180deg, #d6b68c, var(--figure)); }

  .pocket { position: absolute; left: 392px; bottom: 0; width: 392px; height: 178px; }
  .pocket-brand { position: absolute; left: 540px; top: 465px; width: 200px; text-align: center; }
  .pocket-brand .brand-name { font-size: 26px; }
</style>
</head>
<body>
  <section class="spread spread--outer">
    <div class="cover-photo" role="img" aria-label="青空と白い雲の下に広がる草原の写真"></div>
    <div class="fold"></div>
    <div class="cover-brand">
      <p class="brand-tagline">アウトドアライフレンタル</p>
      <p class="brand-name">みなとゆず</p>
      <p class="cover-title">会社案内</p>
    </div>
  </section>

  <section class="spread spread--inner">
    <div class="inner-fold"></div>

    <div class="profile">
      <h2 class="profile-heading">会社概要</h2>
      <ul class="profile-list">
        <li class="label">株式会社みなとゆず</li>
        <li>代表取締役 青木 遥</li>
        <li>設立 2010年4月</li>
        <li>本社</li>
        <li>〒460-0008 名古屋市中区栄町3丁目12番5号</li>
        <li>TEL 052-000-1234　FAX 052-000-1235</li>
        <li>第2倉庫</li>
        <li>〒460-0012 名古屋市中区千歳町2丁目8番1号</li>
        <li>TEL 052-000-2234　FAX 052-000-2235</li>
        <li>資本金 300万円</li>
        <li>ホームページ http://www.minatoyuzu.net</li>
        <li>メール info@minatoyuzu.net</li>
        <li class="gap"></li>
        <li class="label">【業務内容】</li>
        <li>アウトドア用品の販売・レンタル・メンテナンス</li>
        <li>アウトドアレジャーサービスの提供</li>
        <li>イベント・ツアーの企画運営</li>
        <li class="gap"></li>
        <li class="label">【主要取引先】</li>
        <li>株式会社アルト</li>
        <li>株式会社ハルカ</li>
        <li>株式会社ミドリ</li>
        <li>株式会社ナギ</li>
      </ul>
    </div>

    <div class="mission">
      <h2 class="mission-heading">みなとゆず <small>が目指すもの</small></h2>
      <ol class="mission-list">
        <li><span class="num">1</span><span>私たちは、人と人との輪によって、<br>新しい価値を生み出します。</span></li>
        <li><span class="num">2</span><span>私たちは、より良い社会の実現に向けて、<br>豊かな体験をお届けします。</span></li>
        <li><span class="num">3</span><span>私たちは、自然の中で過ごす喜びを、<br>たくさんの方と分かち合います。</span></li>
      </ol>
    </div>

    <div class="hiker" role="img" aria-label="リュックを背負って歩く人物のイラスト"></div>

    <svg class="pocket" viewBox="0 0 392 178" aria-hidden="true">
      <path d="M0 48 L392 0 L392 178 L0 178 Z" fill="#ffffff" stroke="#cfc6bb" stroke-width="1"/>
      <path d="M0 58 L392 12" stroke="#cfc6bb" stroke-width="1" stroke-dasharray="3 3" fill="none"/>
    </svg>
    <div class="pocket-brand">
      <p class="brand-tagline">アウトドアライフレンタル</p>
      <p class="brand-name">みなとゆず</p>
    </div>
  </section>
</body>
</html>
```